Electrical panel service sticker w Bucket truck & Logo

We have a rather plain sticker we put on lighting panels to remind customers who to call for service. We want to redesign them with brushed aluminum background. We want a remake of the sticker with the outline of a bucket truck. You'll need to find or draw the outling of a bucket truck maybe with the boom up slightly as we will get these stickers die cut.

We want LOGO with Ph.# and Email.
Electrical * Lighting * Sign Service

Target Market(s)

Commercial property managers

Industry/Entity Type

Property Management

Requirements
Must have
• Bucket Truck Outline

```html
<!DOCTYPE html>
<html lang="en">
<head>
<meta charset="UTF-8">
<title>Brightline Service Inc. – Panel Service Stickers</title>
<link href="https://fonts.googleapis.com/css2?family=Poppins:wght@600;700;800&family=Roboto:wght@900&display=swap" rel="stylesheet">
<style>
  :root {
    --page: #ffffff;
    --alu-1: #c9cccc;
    --alu-2: #e9ecea;
    --alu-3: #b9bcbd;
    --alu-edge: #9a9d9f;
    --red: #b70f14;
    --blue: #0a2a94;
    --ink: #111111;
    --mono: #2b2b2b;
    --white: #ffffff;
  }
  * { margin: 0; padding: 0; box-sizing: border-box; }
  html, body {
    width: 1091px; height: 1200px; overflow: hidden;
    background: var(--page);
  }
  .canvas { position: relative; width: 1091px; height: 1200px; }

  .sticker {
    position: absolute; left: 98px; width: 888px; height: 390px;
    border-radius: 22px;
    border: 1px solid var(--alu-edge);
    background:
      repeating-linear-gradient(0deg, rgba(255,255,255,.08) 0 1px, rgba(0,0,0,.03) 1px 2px),
      linear-gradient(100deg, var(--alu-1) 0%, var(--alu-2) 38%, var(--alu-3) 62%, var(--alu-2) 82%, var(--alu-1) 100%);
    overflow: hidden;
  }
  .sticker--top { top: 123px; --accent: var(--blue); --name: var(--red); --divider: var(--red); }
  .sticker--bottom { top: 637px; --accent: var(--mono); --name: var(--mono); --divider: var(--mono); }

  .truck-art {
    position: absolute; left: 13px; top: 9px; width: 345px; height: 372px;
    border-radius: 40px 60px 90px 40px;
    background: radial-gradient(ellipse at 55% 60%, var(--accent) 0%, color-mix(in srgb, var(--accent) 55%, transparent) 55%, transparent 80%);
    opacity: .55;
  }

  .info {
    position: absolute; left: 360px; right: 20px; top: 0; bottom: 0;
    text-align: center;
  }
  .brand-name {
    position: absolute; left: 0; right: 0; top: 28px;
    font-family: 'Poppins', sans-serif; font-weight: 800;
    color: var(--name); font-size: 58px; line-height: 1.02;
    letter-spacing: 1px; text-transform: uppercase;
  }
  .phone {
    position: absolute; left: 0; right: 0; top: 226px;
    font-family: 'Roboto', sans-serif; font-weight: 900;
    font-size: 62px; letter-spacing: 2px; color: var(--accent);
    line-height: 1;
  }
  .services {
    position: absolute; left: 0; right: 0; top: 296px;
    font-family: 'Poppins', sans-serif; font-weight: 700;
    font-size: 22px; color: var(--ink); line-height: 1.2;
  }
  .services .divider { color: var(--divider); padding: 0 4px; }
  .email {
    position: absolute; left: 35px; width: 413px; top: 336px; height: 37px;
    border-radius: 19px; background: var(--accent);
    font-family: 'Poppins', sans-serif; font-weight: 700;
    font-size: 17px; color: var(--white); line-height: 37px;
  }
</style>
</head>
<body>
<div class="canvas">

  <section class="sticker sticker--top">
    <div class="truck-art" role="img" aria-label="Die-cut outline illustration of a bucket truck with its boom raised, in blue"></div>
    <div class="info">
      <h1 class="brand-name">Brightline<br>Service Inc.</h1>
      <p class="phone">800·555·0142</p>
      <p class="services">Electrical<span class="divider">|</span>Lighting<span class="divider">|</span>Sign Service</p>
      <p class="email">Service@BrightlineService.com</p>
    </div>
  </section>

  <section class="sticker sticker--bottom">
    <div class="truck-art" role="img" aria-label="Die-cut outline illustration of a bucket truck with its boom raised, in charcoal"></div>
    <div class="info">
      <h1 class="brand-name">Brightline<br>Service Inc.</h1>
      <p class="phone">800·555·0142</p>
      <p class="services">Electrical<span class="divider">|</span>Lighting<span class="divider">|</span>Sign Service</p>
      <p class="email">Service@BrightlineService.com</p>
    </div>
  </section>

</div>
</body>
</html>
```